UI improvement for an existing app

Hi, we have a mobile preorder app that was built with standard flutter UI.

Looking at improving the whole look and feel of our app and make it look more slick and on trend. Something similar to fennoplate, Quorvalo or something along these lines.

Keeping in mind that we are white labeling our app so it needs to be easily redline for other clients.

For our first client I've attached their branding guideline in this project as well.

Please find all the existing screen of our app which we are looking to improve.

Main focus is to give the app a modern and fresh look while making it easy to realign. Do ensure user experience and how they navigate the app is important

Feel free to let me know if you have any questions.

Thanks
KT

Need extra days to review

• All the functionality layout on the screenshot. There's some element that we would like to incorporate such as

1. Coupon code in checkout screen
2. Allow users to edit their profile in profile page

```html
<!DOCTYPE html>
<html lang="en">
<head>
<meta charset="utf-8">
<title>Preorder App – Screen Overview</title>
<link href="https://fonts.googleapis.com/css2?family=Roboto:wght@400;500;700&family=Poppins:wght@500;600&display=swap" rel="stylesheet">
<style>
:root{
  --bg:#f7f7f2;
  --card:#ffffff;
  --green:#8cb81f;
  --green-soft:#e9f3d2;
  --ink:#222222;
  --muted:#6f6f6f;
  --line:#eeeeee;
  --chip:#f3f3f0;
  --red:#f04a4a;
  --yellow:#f5e22a;
  --done:#2fe06a;
  --social:#3d5598;
}
*{box-sizing:border-box;margin:0;padding:0}
html,body{width:711px;height:1200px;overflow:hidden;background:var(--bg)}
body{font-family:'Roboto',sans-serif;color:var(--ink)}
.board{position:absolute;left:0;top:0;width:1484px;height:2505px;transform:scale(.4791);transform-origin:0 0}
.screen{position:absolute;width:290px;height:627px;background:var(--card);border-radius:30px;overflow:hidden;box-shadow:0 8px 30px rgba(0,0,0,.03)}
.a{position:absolute}
.caption{position:absolute;width:290px;text-align:center;font-family:'Poppins',sans-serif;font-weight:600;font-size:18px;color:var(--ink)}
.btn{position:absolute;border-radius:22px;background:var(--green);color:#fff;font-weight:700;font-size:11px;display:flex;align-items:center;justify-content:center;gap:7px;box-shadow:0 6px 12px rgba(140,184,31,.3)}
.g{color:var(--green)}
.pill{position:absolute;border-radius:14px;font-size:10px;display:flex;align-items:center;justify-content:center}
.pill.on{background:var(--green);color:#fff}
.pill.off{background:var(--chip);color:var(--ink)}
.nav{position:absolute;height:44px;background:#fff;border-radius:22px;box-shadow:0 4px 14px rgba(0,0,0,.08);display:flex;justify-content:space-around;align-items:center;padding:0 10px}
.nav svg{width:16px;height:16px;fill:#333}
.nav svg.cur{fill:var(--green)}
.photo{position:absolute}
.heart{position:absolute;width:14px;height:14px;border-radius:50%;background:#fff;display:flex;align-items:center;justify-content:center}
.product .name{position:absolute;width:78px;text-align:center;font-size:8.5px;color:var(--muted);line-height:10px}
.product .price{position:absolute;width:78px;text-align:center;font-size:11px;font-weight:700;color:var(--green)}
.opt{position:absolute;width:80px;height:45px;border-radius:6px;background:var(--chip);color:var(--green);font-size:10.5px;font-weight:700;display:flex;flex-direction:column;align-items:center;justify-content:center;line-height:16px}
.opt small{color:var(--muted);font-weight:400;font-size:10px}
.opt.sel{background:#fff;border:1.5px solid var(--green)}
.label{position:absolute;font-size:12px;color:var(--ink);font-weight:500}
.row{position:absolute;left:0;width:100%;display:flex;justify-content:space-between;font-size:10.5px;color:var(--muted)}
.row b{font-weight:500;color:var(--green)}
.order{position:absolute;left:21px;width:248px;height:100px;background:#fff;border-radius:8px;box-shadow:0 3px 12px rgba(0,0,0,.05)}
.bag{position:absolute;width:28px;height:28px;border-radius:50%;background:var(--green);display:flex;align-items:center;justify-content:center}
.bag svg{width:12px;height:12px;fill:#fff}
.status{position:absolute;right:11px;top:12px;height:22px;padding:0 15px;border-radius:11px;font-size:9px;color:#fff;display:flex;align-items:center}
.order .no{position:absolute;left:11px;top:54px;font-size:10px;font-weight:700;color:var(--green)}
.order .txt{position:absolute;left:11px;top:68px;font-size:9px;line-height:14px;color:var(--ink)}
.order .amt{position:absolute;right:11px;top:70px;font-size:11px;font-weight:700;color:var(--green)}
.prow{position:absolute;left:11px;right:11px;height:39px;display:flex;justify-content:space-between;align-items:center;font-size:11px;color:var(--muted);border-bottom:1px solid var(--line);font-family:'Poppins',sans-serif}
.prow b{font-weight:500;color:var(--green)}
</style>
</head>
<body>
<div class="board">

<!-- Login -->
<section class="screen" style="left:108px;top:100px">
  <div class="a" style="left:72px;top:88px;display:flex;align-items:center;gap:8px">
    <span style="font-family:'Roboto',sans-serif;font-weight:700;font-size:32px;color:#2f2f2f">Leafora</span>
    <span style="width:24px;height:24px;border-radius:50%;background:var(--green)"></span>
  </div>
  <div class="a" style="left:120px;top:146px;font-size:9px;color:#333">Stay fresh</div>
  <div class="a" style="left:20px;top:215px;width:250px;height:80px;border-radius:6px;box-shadow:0 2px 12px rgba(0,0,0,.06)">
    <div class="a" style="left:12px;top:15px;font-size:10.5px;color:var(--muted)">Username/email</div>
    <div class="a" style="left:0;top:39px;width:100%;border-top:1px solid var(--line)"></div>
    <div class="a" style="left:12px;top:53px;font-size:10.5px;color:var(--muted)">Password</div>
    <svg class="a" style="left:222px;top:55px" width="14" height="8" viewBox="0 0 14 8"><path d="M1 1q6 7 12 0M3 5l-1 2M7 6v2M11 5l1 2" stroke="#8cb81f" stroke-width="1.3" fill="none"/></svg>
  </div>
  <div class="a g" style="left:0;width:100%;top:314px;text-align:center;font-size:10px;font-weight:500">Forgot password?</div>
  <div class="btn" style="left:52px;top:374px;width:186px;height:38px">Login with email</div>
  <div class="a" style="left:48px;top:456px;width:82px;border-top:1px solid #cfe3a0"></div>
  <div class="a" style="left:0;width:100%;top:451px;text-align:center;font-size:10px;color:#444">OR</div>
  <div class="a" style="left:161px;top:456px;width:82px;border-top:1px solid #cfe3a0"></div>
  <div class="btn" style="left:52px;top:499px;width:186px;height:38px;background:var(--social);box-shadow:0 6px 12px rgba(61,85,152,.3)"><span style="width:12px;height:12px;background:#fff;border-radius:2px"></span>Login with Linkbook</div>
  <div class="a" style="left:0;width:100%;top:595px;text-align:center;font-size:10px;color:#333">Don't have an account? <b class="g" style="font-weight:500">Signup</b></div>
</section>
<div class="caption" style="left:108px;top:776px">Login</div>

<!-- Home -->
<section class="screen" style="left:597px;top:100px">
  <div class="photo" role="img" aria-label="Promotional banner with strawberry dessert" style="left:21px;top:35px;width:248px;height:115px;border-radius:8px;background:linear-gradient(100deg,#285a56 0 48%,#f3c9c4 62%,#e2534f 100%)">
    <div class="a" style="left:32px;top:6px;font-family:Georgia,serif;font-size:8.5px;font-weight:700;color:#fff;line-height:10px">Strawberry Desserts<br>for Less</div>
    <div class="a" style="left:32px;top:36px;font-size:14px;color:#fff">BUY 2 GET 1</div>
    <div class="a" style="left:32px;top:53px;font-size:5px;color:#fff">for a Limited Time</div>
  </div>
  <div class="btn" style="left:21px;top:162px;width:248px;height:46px;border-radius:23px;font-size:12px">
    <svg width="16" height="14" viewBox="0 0 16 14"><path d="M1 2v5l7 7 7-7-7-7H2z" fill="none" stroke="#fff" stroke-width="1.6"/><circle cx="4.5" cy="4" r="1.3" fill="#fff"/></svg>987.38 - Free Drinks Available!</div>
  <div class="a" style="left:25px;top:220px;width:240px;height:215px;border-radius:6px;box-shadow:0 3px 12px rgba(0,0,0,.06);overflow:hidden">
    <div class="photo" role="img" aria-label="Restaurant interior with tables and drinks" style="left:0;top:0;width:240px;height:140px;background:linear-gradient(180deg,#6e5848,#3b3229 70%,#2c2722)"></div>
    <div class="heart" style="left:208px;top:8px;width:24px;height:24px"><svg width="12" height="11" viewBox="0 0 12 11"><path d="M6 10L1 5a3 3 0 015-4 3 3 0 015 4z" fill="#8cb81f"/></svg></div>
    <div class="pill on" style="left:8px;top:106px;width:66px;height:26px;font-size:9.5px">Open</div>
    <div class="a" style="left:8px;top:150px;font-size:16.5px;font-weight:500">Leafora Carousel</div>
    <div class="a" style="left:8px;top:186px;display:flex;align-items:center;gap:6px;font-size:9px;color:var(--muted)"><span style="width:14px;height:14px;border-radius:50%;background:var(--green)"></span>05 Min.<svg style="margin-left:12px" width="10" height="13" viewBox="0 0 10 13"><path d="M5 13S0 7 0 5a5 5 0 0110 0c0 2-5 8-5 8z" fill="#8cb81f"/><circle cx="5" cy="5" r="1.8" fill="#fff"/></svg>1.50 KM</div>
  </div>
  <div class="a" style="left:25px;top:446px;width:240px;height:190px;border-radius:6px;overflow:hidden">
    <div class="photo" role="img" aria-label="Iced milk drink in a glass" style="left:0;top:0;width:240px;height:140px;background:linear-gradient(110deg,#5b5044,#b8ab9a 45%,#40433e)"></div>
    <div class="pill on" style="left:8px;top:106px;width:66px;height:26px"></div>
    <div class="a" style="left:8px;top:150px;font-size:16.5px;font-weight:500">Eastmoor Kitchen</div>
  </div>
  <nav class="nav" style="left:37px;top:563px;width:216px">
    <svg class="cur" viewBox="0 0 16 16"><path d="M8 2l6 6h-2v6H9v-4H7v4H4V8H2z"/></svg>
    <svg viewBox="0 0 16 16"><path d="M1 2v6l7 7 7-7-7-7H2zm3 1.5a1.5 1.5 0 110 3 1.5 1.5 0 010-3z"/></svg>
    <svg viewBox="0 0 16 16"><path d="M3 1h10v14H3zm2 3h6v1H5zm0 3h6v1H5zm0 3h6v1H5z" fill-rule="evenodd"/></svg>
    <svg viewBox="0 0 16 16"><path d="M1 3h14v10H1zm1.5 1.5v1.5h11V4.5zm0 4v3h11v-3z" fill-rule="evenodd"/></svg>
    <svg viewBox="0 0 16 16"><circle cx="8" cy="5" r="3"/><path d="M2 15c0-4 3-6 6-6s6 2 6 6z"/></svg>
  </nav>
</section>
<div class="caption" style="left:597px;top:776px">Home Screen</div>

<!-- Shop details -->
<section class="screen" style="left:1086px;top:100px">
  <div class="photo" role="img" aria-label="Restaurant interior" style="left:0;top:0;width:290px;height:185px;background:linear-gradient(180deg,#7a6656,#4a3d33 60%,#2e2823)"></div>
  <svg class="a" style="left:14px;top:38px" width="14" height="12" viewBox="0 0 14 12"><path d="M13 6H2M6 1L1 6l5 5" stroke="#fff" stroke-width="1.6" fill="none"/></svg>
  <div class="pill on" style="left:13px;top:88px;width:66px;height:26px;font-size:9.5px">Open</div>
  <div class="a" style="left:13px;top:123px;font-size:17px;font-weight:700;color:#fff">Leafora Carousel</div>
  <div class="a" style="left:14px;top:156px;display:flex;align-items:center;gap:5px;font-size:9px;color:#fff"><span style="width:14px;height:14px;border-radius:50%;background:#fff"></span>05 Min.<svg style="margin-left:12px" width="10" height="13" viewBox="0 0 10 13"><path d="M5 13S0 7 0 5a5 5 0 0110 0c0 2-5 8-5 8z" fill="#fff"/></svg>1.50 KM</div>
  <div class="a" style="left:28px;top:218px;font-size:12px;font-weight:500">Details</div>
  <div class="a" style="left:239px;top:217px;width:17px;height:17px;border-radius:50%;background:var(--green-soft)"><svg class="a" style="left:5px;top:6px" width="7" height="5" viewBox="0 0 7 5"><path d="M0 0h7L3.5 5z" fill="#8cb81f"/></svg></div>
  <div class="pill on" style="left:13px;top:266px;width:84px;height:27px">All Items</div>
  <div class="pill off" style="left:106px;top:266px;width:121px;height:27px">Relish Fresh Tea</div>
  <div class="pill off" style="left:236px;top:266px;width:60px;height:27px;justify-content:flex-start;padding-left:20px">Milk</div>
  <div class="product">
    <div class="photo" role="img" aria-label="Cocoa drink cup" style="left:21px;top:312px;width:78px;height:95px;background:#a7cdf0;border-radius:4px 4px 0 0"></div>
    <div class="photo" role="img" aria-label="Pearl milk tea cup" style="left:106px;top:312px;width:78px;height:95px;background:#a3e8c8;border-radius:4px 4px 0 0"></div>
    <div class="photo" role="img" aria-label="Black tea cup" style="left:191px;top:312px;width:78px;height:95px;background:#f4eaa8;border-radius:4px 4px 0 0"></div>
    <div class="heart" style="left:79px;top:318px"><svg width="8" height="7" viewBox="0 0 12 11"><path d="M6 10L1 5a3 3 0 015-4 3 3 0 015 4z" fill="none" stroke="#333" stroke-width="1.4"/></svg></div>
    <div class="heart" style="left:164px;top:318px"><svg width="8" height="7" viewBox="0 0 12 11"><path d="M6 10L1 5a3 3 0 015-4 3 3 0 015 4z" fill="none" stroke="#333" stroke-width="1.4"/></svg></div>
    <div class="heart" style="left:249px;top:318px"><svg width="8" height="7" viewBox="0 0 12 11"><path d="M6 10L1 5a3 3 0 015-4 3 3 0 015 4z" fill="none" stroke="#333" stroke-width="1.4"/></svg></div>
    <div class="name" style="left:21px;top:413px">Cocoa Crunchy Ice</div>
    <div class="name" style="left:106px;top:413px">Special Pearl Milk Tea</div>
    <div class="name" style="left:191px;top:413px">Ceylob Black Tea</div>
    <div class="price" style="left:21px;top:437px">$12.00</div>
    <div class="price" style="left:106px;top:437px">$19.55</div>
    <div class="price" style="left:191px;top:437px">$10.50</div>
    <div class="photo" role="img" aria-label="Milk tea cup" style="left:21px;top:463px;width:78px;height:95px;background:#e7a3ea;border-radius:4px 4px 0 0"></div>
    <div class="photo" role="img" aria-label="Fruit tea cup" style="left:106px;top:463px;width:78px;height:95px;background:#f4c99a;border-radius:4px 4px 0 0"></div>
    <div class="photo" role="img" aria-label="Mango drink cup" style="left:191px;top:463px;width:78px;height:95px;background:#c9a8f0;border-radius:4px 4px 0 0"></div>
    <div class="heart" style="left:79px;top:469px"><svg width="8" height="7" viewBox="0 0 12 11"><path d="M6 10L1 5a3 3 0 015-4 3 3 0 015 4z" fill="none" stroke="#333" stroke-width="1.4"/></svg></div>
    <div class="heart" style="left:164px;top:469px"><svg width="8" height="7" viewBox="0 0 12 11"><path d="M6 10L1 5a3 3 0 015-4 3 3 0 015 4z" fill="none" stroke="#333" stroke-width="1.4"/></svg></div>
    <div class="heart" style="left:249px;top:469px"><svg width="8" height="7" viewBox="0 0 12 11"><path d="M6 10L1 5a3 3 0 015-4 3 3 0 015 4z" fill="none" stroke="#333" stroke-width="1.4"/></svg></div>
  </div>
  <div class="btn" style="left:36px;top:562px;width:217px;height:46px;border-radius:23px;font-size:12.5px">
    <svg width="16" height="14" viewBox="0 0 16 14"><path d="M0 1h3l2 8h9l2-6H4" fill="none" stroke="#fff" stroke-width="1.6"/><circle cx="6" cy="12" r="1.5" fill="#fff"/><circle cx="13" cy="12" r="1.5" fill="#fff"/></svg>Shopping Cart $24.80</div>
</section>
<div class="caption" style="left:1086px;top:776px">Shop Details</div>

<!-- Item details -->
<section class="screen" style="left:108px;top:901px">
  <div class="a" style="left:0;top:0;width:290px;height:187px;background:#a5cdef"></div>
  <svg class="a" style="left:16px;top:38px" width="14" height="12" viewBox="0 0 14 12"><path d="M13 6H2M6 1L1 6l5 5" stroke="#fff" stroke-width="1.6" fill="none"/></svg>
  <div class="photo" role="img" aria-label="Cocoa crunchy ice drink" style="left:124px;top:48px;width:36px;height:76px;border-radius:4px 4px 8px 8px;background:linear-gradient(180deg,#e8d9cc,#b7764f)"></div>
  <div class="a" style="left:13px;top:135px;font-size:17px;font-weight:700;color:#fff">Cocoa Crunchy Ice</div>
  <div class="a" style="left:13px;top:160px;font-size:11.5px;font-weight:500;color:#fff">Yummy Milkshake with Crunchy Chocolate</div>
  <div class="label" style="left:13px;top:209px">Size</div>
  <div class="opt sel" style="left:13px;top:232px">Medium<small>250 ml</small></div>
  <div class="opt" style="left:103px;top:232px">Large<small>500 ml</small></div>
  <div class="label" style="left:13px;top:312px">Sweetness</div>
  <div class="opt sel" style="left:13px;top:336px">100%</div>
  <div class="opt" style="left:104px;top:336px">75%</div>
  <div class="opt" style="left:196px;top:336px">50%</div>
  <div class="opt" style="left:288px;top:336px"></div>
  <div class="label" style="left:13px;top:415px">Ice</div>
  <div class="opt sel" style="left:13px;top:438px">Full Ice</div>
  <div class="opt" style="left:104px;top:438px">Less Ice</div>
  <div class="opt" style="left:196px;top:438px">No Ice</div>
  <div class="a" style="left:38px;top:563px;width:214px;height:44px;border-radius:22px;background:#fff;box-shadow:0 4px 14px rgba(0,0,0,.08)">
    <span class="a" style="left:10px;top:15px;font-size:10.5px">Item Total:</span>
    <span class="a g" style="left:75px;top:12px;font-size:14.5px;font-weight:700">$12.00</span>
    <span class="a" style="left:147px;top:11px;width:22px;height:22px;border-radius:50%;background:#fde6e6;color:var(--red);font-size:13px;text-align:center;line-height:22px">✕</span>
    <span class="a" style="left:180px;top:11px;width:22px;height:22px;border-radius:50%;background:var(--green)"><svg class="a" style="left:6px;top:7px" width="10" height="8" viewBox="0 0 10 8"><path d="M1 4l3 3 5-6" stroke="#fff" stroke-width="1.6" fill="none"/></svg></span>
  </div>
</section>
<div class="caption" style="left:108px;top:1576px">Item Details</div>

<!-- Checkout -->
<section class="screen" style="left:597px;top:901px">
  <svg class="a" style="left:16px;top:38px" width="14" height="12" viewBox="0 0 14 12"><path d="M13 6H2M6 1L1 6l5 5" stroke="#222" stroke-width="1.6" fill="none"/></svg>
  <div class="a" style="left:0;width:100%;top:37px;text-align:center;font-size:11px">Checkout</div>
  <div class="a" style="left:21px;top:85px;width:248px;height:148px;border-radius:6px;box-shadow:0 3px 12px rgba(0,0,0,.05)">
    <div class="a g" style="left:12px;top:12px;font-size:17px;font-weight:700">$12.00</div>
    <div class="a" style="left:12px;top:37px;font-size:12px;font-weight:500">Cocoa Crunchy Ice</div>
    <div class="a" style="left:12px;top:59px;font-size:10px">Medium <span class="g">●</span> 100% Sweet <span class="g">●</span> Full Ice</div>
    <span class="a" style="left:222px;top:10px;width:18px;height:18px;border-radius:50%;background:#f9b7b7"><span class="a" style="left:5px;top:8px;width:8px;border-top:1.5px solid var(--red)"></span></span>
    <span class="a" style="left:85px;top:93px;width:18px;height:18px;border-radius:50%;background:#fbd0d0"><span class="a" style="left:5px;top:8px;width:8px;border-top:1.5px solid var(--red)"></span></span>
    <span class="a" style="left:117px;top:95px;font-size:10px">01</span>
    <span class="a g" style="left:146px;top:93px;width:18px;height:18px;border-radius:50%;background:var(--green-soft);text-align:center;line-height:18px;font-size:13px">+</span>
    <span class="a" style="left:8px;top:122px;font-size:10px;color:var(--muted)">Use Royalty Points</span>
    <span class="a" style="left:206px;top:121px;width:35px;height:15px;border-radius:8px;background:var(--green)"><span class="a" style="left:22px;top:3px;width:9px;height:9px;border-radius:50%;background:#fff"></span></span>
  </div>
  <div class="a g" style="left:21px;top:245px;width:248px;height:46px;border:1.5px dashed var(--green);border-radius:6px;display:flex;align-items:center;justify-content:center;font-size:12px;font-weight:700">Add more items</div>
  <div class="a" style="left:0;top:432px;width:100%;border-top:2px solid #f4f4f4"></div>
  <div class="row" style="top:443px;padding:0 13px">Your Wallet<b>$500.00</b></div>
  <div class="row" style="top:470px;padding:0 13px">Royalty Points<b>987.38</b></div>
  <div class="a" style="left:21px;top:504px;width:248px;height:38px;border:1px solid #e6e6e6;border-radius:6px">
    <span class="a" style="left:11px;top:12px;font-size:10.5px;color:var(--muted)">Enter coupon code</span>
    <span class="a" style="left:215px;top:7px;width:24px;height:24px;border-radius:3px;background:var(--green)"><svg class="a" style="left:6px;top:7px" width="12" height="10" viewBox="0 0 14 12"><path d="M1 6h11M8 1l5 5-5 5" stroke="#fff" stroke-width="1.8" fill="none"/></svg></span>
  </div>
  <div class="btn" style="left:52px;top:570px;width:186px;height:38px">Place Order - $12.00</div>
</section>
<div class="caption" style="left:597px;top:1576px">Checkout</div>

<!-- Orders -->
<section class="screen" style="left:1086px;top:901px">
  <div class="a" style="left:0;top:62px;font-size:6px;color:#888">0</div>
  <div class="a" style="left:21px;top:35px;width:248px;height:62px;border-radius:6px;background:#fff;box-shadow:0 3px 12px rgba(0,0,0,.05)">
    <div class="bag" style="left:10px;top:17px"><svg viewBox="0 0 12 12"><path d="M1 4h10v8H1zM4 4V2a2 2 0 014 0v2" /></svg></div>
    <div class="a" style="left:47px;top:17px;font-size:9px;font-weight:500">Leafora Quarry Lane (1 item)</div>
    <div class="a" style="left:47px;top:32px;font-size:8.5px">#8 <span class="g">●</span> 07:15 PM <span class="g">●</span> 15 - July - 2020</div>
    <div class="a g" style="left:210px;top:24px;font-size:10.5px;font-weight:700">$6.80</div>
  </div>
  <div class="a" style="left:286px;top:56px;width:8px;height:18px;border-radius:4px;background:var(--green)"></div>
  <div class="a" style="left:134px;top:108px;display:flex;gap:4px"><span style="width:4px;height:4px;border-radius:50%;background:#e0eec0"></span><span style="width:4px;height:4px;border-radius:50%;background:var(--green)"></span><span style="width:4px;height:4px;border-radius:50%;background:#e0eec0"></span></div>
  <div class="a" style="left:21px;top:130px;width:248px;height:38px;border:1px solid #e6e6e6;border-radius:6px">
    <svg class="a" style="left:12px;top:12px" width="12" height="12" viewBox="0 0 12 12"><circle cx="5" cy="5" r="3.8" fill="none" stroke="#333" stroke-width="1.4"/><path d="M8 8l3 3" stroke="#333" stroke-width="1.6"/></svg>
    <span class="a" style="left:34px;top:12px;font-size:10.5px;color:var(--muted)">Search Orders</span>
  </div>
  <div class="pill on" style="left:13px;top:199px;width:89px;height:27px">All Orders</div>
  <div class="pill off" style="left:112px;top:199px;width:92px;height:27px">In Progress</div>
  <div class="pill off" style="left:214px;top:199px;width:92px;height:27px">Completed</div>
  <div class="order" style="top:258px">
    <div class="bag" style="left:11px;top:12px"><svg viewBox="0 0 12 12"><path d="M1 4h10v8H1zM4 4V2a2 2 0 014 0v2"/></svg></div>
    <div class="status" style="background:var(--done)">Completed</div>
    <div class="no">#8</div>
    <div class="txt">Leafora Quarry Lane (1 item)<br>07:15 PM <span class="g">●</span> 15 - July - 2020</div>
    <div class="amt">$6.80</div>
  </div>
  <div class="order" style="top:376px">
    <div class="bag" style="left:11px;top:12px"><svg viewBox="0 0 12 12"><path d="M1 4h10v8H1zM4 4V2a2 2 0 014 0v2"/></svg></div>
    <div class="status" style="background:var(--yellow)">In Progress</div>
    <div class="no">#7</div>
    <div class="txt">Leafora Quarry Lane (1 item)<br>09:10 AM <span class="g">●</span> 14 - July - 2020</div>
    <div class="amt">$9.99</div>
  </div>
  <div class="order" style="top:493px">
    <div class="bag" style="left:11px;top:12px"><svg viewBox="0 0 12 12"><path d="M1 4h10v8H1zM4 4V2a2 2 0 014 0v2"/></svg></div>
    <div class="status" style="background:var(--red)">Cancelled</div>
    <div class="no">#6</div>
    <div class="txt">Leafora Quarry Lane (1 item)<br>0</div>
  </div>
  <nav class="nav" style="left:36px;top:563px;width:217px">
    <svg viewBox="0 0 16 16"><path d="M8 2l6 6h-2v6H9v-4H7v4H4V8H2z"/></svg>
    <svg viewBox="0 0 16 16"><path d="M1 2v6l7 7 7-7-7-7H2zm3 1.5a1.5 1.5 0 110 3 1.5 1.5 0 010-3z"/></svg>
    <svg class="cur" viewBox="0 0 16 16"><path d="M3 1h10v14H3zm2 3h6v1H5zm0 3h6v1H5zm0 3h6v1H5z" fill-rule="evenodd"/></svg>
    <svg viewBox="0 0 16 16"><path d="M1 3h14v10H1zm1.5 1.5v1.5h11V4.5zm0 4v3h11v-3z" fill-rule="evenodd"/></svg>
    <svg viewBox="0 0 16 16"><circle cx="8" cy="5" r="3"/><path d="M2 15c0-4 3-6 6-6s6 2 6 6z"/></svg>
  </nav>
</section>
<div class="caption" style="left:1086px;top:1576px">Orders</div>

<!-- Profile -->
<section class="screen" style="left:597px;top:1702px">
  <div class="a" style="left:0;width:100%;top:60px;text-align:center;font-family:'Poppins',sans-serif;font-weight:600;font-size:14px">Owen Carter</div>
  <div class="a" style="left:0;width:100%;top:88px;text-align:center;font-family:'Poppins',sans-serif;font-size:11px;color:var(--muted)">Harbourton</div>
  <div class="a" style="left:21px;top:140px;width:248px;height:322px;border-radius:6px;box-shadow:0 3px 12px rgba(0,0,0,.05)">
    <div class="a" style="left:8px;top:10px;font-family:'Poppins',sans-serif;font-size:12.5px;font-weight:500">Personal</div>
    <div class="prow" style="top:35px">First Name<b>Owen</b></div>
    <div class="prow" style="top:74px">Last Name<b>Carter</b></div>
    <div class="prow" style="top:113px">Account Type<b>Email</b></div>
    <div class="prow" style="top:152px">User ID<b>139</b></div>
    <div class="prow" style="top:191px">Wallet ID<b>7623</b></div>
    <div class="prow" style="top:230px;border-bottom:none">Mobile Verified<b>Yes</b></div>
    <div class="a g" style="left:0;width:100%;top:287px;text-align:center;font-family:'Poppins',sans-serif;font-size:11px;text-decoration:underline">Edit Profile</div>
  </div>
  <div class="btn" style="left:52px;top:490px;width:186px;height:38px">Contact Us</div>
  <nav class="nav" style="left:37px;top:563px;width:216px">
    <svg viewBox="0 0 16 16"><path d="M8 2l6 6h-2v6H9v-4H7v4H4V8H2z"/></svg>
    <svg viewBox="0 0 16 16"><path d="M1 2v6l7 7 7-7-7-7H2zm3 1.5a1.5 1.5 0 110 3 1.5 1.5 0 010-3z"/></svg>
    <svg viewBox="0 0 16 16"><path d="M3 1h10v14H3zm2 3h6v1H5zm0 3h6v1H5zm0 3h6v1H5z" fill-rule="evenodd"/></svg>
    <svg viewBox="0 0 16 16"><path d="M1 3h14v10H1zm1.5 1.5v1.5h11V4.5zm0 4v3h11v-3z" fill-rule="evenodd"/></svg>
    <svg class="cur" viewBox="0 0 16 16"><circle cx="8" cy="5" r="3"/><path d="M2 15c0-4 3-6 6-6s6 2 6 6z"/></svg>
  </nav>
</section>
<div class="caption" style="left:597px;top:2377px">Checkout</div>

</div>
</body>
</html>
```